Window Tinting Website Design

We are working with a Window Tinting company in California. They do commercial, residential, and automotive tint.

Some websites for inspiration:
https://www.velofilmz.com/
https://www.tkglossbay.com/
https://orbishadez.com/

Thank you for taking the time to consider designing a website for us. We are web developers based in Stockton, CA, USA. Most of our projects go through the same process. Understanding this process may help you win a project with us. We custom-code all of our websites in-house. We don’t have any requirements as to what tools you use for your design, but we ask that you follow these guidelines.

IMAGES:
If you use any images or icons in the design, we ask that you have a link to the asset so we can purchase the image/icon. Most of the designs we submit do not have the customer’s images on them unless they have some great images. Be creative; show us the feeling you are trying to portray with your image choices. Use any royalty-free site you choose. We subscribe to Brellix and mainly use their images, but we can purchase images outside of Brellix. PLEASE NOTE: we will not submit designs to clients with watermarks on the images.

FONTS:
We ask that you identify the fonts you’re using in the design. This can be done in a message if you want. We typically use Tarvo Fonts and Brellix Fonts.

CONTENT:
We're always open to different content and ideas. We often submit designs with stock images so the client can see our vision. We typically take pictures after the website launch to use their images with our vision. Lorem Ipsum is fine for paragraphs, but we ask that you make the Headers with correct English. We want to be able to show the vision and identify the sections of the website.

INSPIRATION:
We typically add a couple of links in the brief of websites we like to help you get started in your design.

REVISIONS:
We do not often ask for revisions of the designs unless we see something in the design that may not appeal to the client. If there are slight changes that we want to make, we do that in the development process.

FEEDBACK:
We rarely give feedback on designs during the design process. We are working on many website projects and do not have the time to provide feedback. We usually respond if your request is well thought out and asks specific questions, but a note asking “feedback, please” usually goes unanswered.

```html
<!DOCTYPE html>
<html lang="en">
<head>
<meta charset="utf-8">
<title>Apex Shade Tinting</title>
<link href="https://fonts.googleapis.com/css2?family=Poppins:ital,wght@0,400;0,600;0,700;0,800;1,800&family=Lato:wght@400;700&display=swap" rel="stylesheet">
<style>
:root{
  --red:#c8102e;
  --red-dark:#8e0a1f;
  --black:#0b0b0b;
  --ink:#161616;
  --white:#ffffff;
  --grey:#bdbdbd;
}
*{margin:0;padding:0;box-sizing:border-box}
html,body{width:1200px;height:3936px;overflow:hidden}
body{background:var(--black);font-family:"Lato",sans-serif;color:var(--white);position:relative}
section,header,footer{position:absolute;left:0;width:1200px}
.eyebrow{font-family:"Poppins",sans-serif;font-weight:800;font-style:italic;font-size:16px;letter-spacing:2px;text-transform:uppercase;text-align:center}
.section-title{font-family:"Poppins",sans-serif;font-weight:800;font-size:36px;text-transform:uppercase;text-align:center;margin-top:6px}
.section-title span{color:var(--red)}
.btn{display:inline-block;font-family:"Poppins",sans-serif;font-weight:700;font-size:15px;padding:16px 30px;border-radius:4px;text-transform:uppercase}
.btn-white{background:var(--white);color:var(--red)}
.btn-red{background:var(--red);color:var(--white)}
.brand-name{font-family:"Poppins",sans-serif;font-weight:800;color:var(--white);text-transform:uppercase;display:flex;align-items:center;gap:10px}
.brand-name i{display:block;width:14px;height:14px;background:var(--white);border-radius:50%}

/* Hero */
.hero{top:0;height:700px;background:#111}
.hero-photo{position:absolute;left:0;top:0;width:1200px;height:680px;
  background:
    radial-gradient(ellipse 260px 200px at 860px 190px,rgba(222,170,140,.85),rgba(222,170,140,0) 70%),
    radial-gradient(ellipse 200px 160px at 1060px 330px,rgba(200,150,120,.75),rgba(200,150,120,0) 70%),
    radial-gradient(ellipse 520px 380px at 880px 260px,#c9c9c9 0%,#8a8a8a 40%,rgba(60,60,60,0) 80%),
    linear-gradient(100deg,#141414 0%,#262626 40%,#4d4d4d 70%,#2a2a2a 100%)}
.hero-shade{position:absolute;left:0;top:0;width:700px;height:680px;background:linear-gradient(90deg,rgba(10,10,10,.85),rgba(10,10,10,0))}
.topbar{position:absolute;top:0;left:0;width:1200px;height:80px;background:rgba(0,0,0,.55)}
.social{position:absolute;left:110px;top:16px;display:flex;gap:12px}
.social i{width:12px;height:12px;border-radius:50%;background:var(--white);display:block}
.contact-mini{position:absolute;right:110px;top:14px;display:flex;gap:22px;font-size:13px}
.contact-mini span{display:flex;align-items:center;gap:7px}
.nav{position:absolute;top:54px;font-family:"Poppins",sans-serif;font-weight:700;font-size:15px;text-transform:uppercase;display:flex;gap:60px}
.nav-left{left:110px}
.nav-left .active{color:var(--red);border-bottom:2px solid var(--red)}
.nav-right{right:110px;top:48px;align-items:center}
.nav-right .btn{padding:10px 16px;font-size:14px}
.nav-brand{position:absolute;left:485px;top:0;width:230px;height:120px;background:var(--red);border:4px solid var(--white);border-top:none;border-radius:0 0 18px 18px;display:flex;align-items:center;justify-content:center}
.nav-brand .brand-name{font-size:20px;text-align:center;line-height:1.1}
.hero-copy{position:absolute;left:110px;top:200px;width:560px}
.hero-copy .kicker{font-family:"Poppins",sans-serif;font-weight:800;font-style:italic;font-size:16px;letter-spacing:2px}
.hero-copy h1{font-family:"Poppins",sans-serif;font-weight:800;font-size:40px;line-height:1.2;margin:14px 0 20px;text-transform:uppercase}
.hero-copy p{font-size:15px;line-height:1.6;color:#e6e6e6;margin-bottom:28px;width:460px}
.slider-dots{position:absolute;left:576px;top:600px;display:flex;gap:14px}
.slider-dots i{width:12px;height:12px;border-radius:50%;background:#888;display:block}
.slider-dots i.on{background:var(--white)}
.hero-chevron{position:absolute;left:0;top:540px}

/* About */
.about{top:700px;height:730px;background:var(--white);color:var(--ink)}
.about .eyebrow{margin-top:95px;color:var(--ink)}
.about .section-title{color:var(--ink)}
.about-brand{position:absolute;left:120px;top:210px;width:470px;height:180px;background:var(--red);border-radius:14px;display:flex;align-items:center;justify-content:center}
.about-brand .brand-name{font-size:36px}
.about-text{position:absolute;left:650px;top:190px;width:420px;font-size:14.5px;line-height:1.65;color:#333}
.about-text p{margin-bottom:16px}
.about-text .btn{margin-top:6px;background:var(--white);color:var(--red);border:1px solid var(--red);box-shadow:0 4px 14px rgba(0,0,0,.15)}
.stats{position:absolute;left:110px;top:530px;width:980px;display:flex}
.stat{flex:1;text-align:center;border-right:1px solid #d5d5d5}
.stat:last-child{border-right:none}
.stat strong{display:block;font-family:"Poppins",sans-serif;font-weight:400;font-size:52px;color:var(--ink);line-height:1.1}
.stat span{display:block;font-size:14px;line-height:1.5;margin-top:8px;color:#333}

/* Services */
.services{top:1430px;height:810px;background:var(--black)}
.services .eyebrow{margin-top:100px}
.service{position:absolute;width:290px;text-align:center}
.service .photo{height:330px;width:290px;border-radius:3px}
.service h3{font-family:"Poppins",sans-serif;font-weight:700;font-size:15px;text-transform:uppercase;margin:20px 0 10px}
.service p{font-size:13px;line-height:1.55;color:var(--grey);padding:0 12px}
.svc-commercial{left:100px;top:210px}
.svc-commercial .photo{background:
  radial-gradient(ellipse 70px 60px at 90px 70px,#a47a5f,rgba(164,122,95,0) 75%),
  radial-gradient(ellipse 110px 150px at 80px 220px,#8fa3b4,rgba(143,163,180,0) 75%),
  linear-gradient(90deg,#f2f5f8 0%,#dfe7ee 45%,#3a3f44 46%,#4a5055 52%,#cfd9e2 53%,#eef2f5 100%)}
.svc-residential{left:455px;top:280px}
.svc-residential .photo{background:
  radial-gradient(ellipse 60px 55px at 145px 90px,#6d4b3a,rgba(109,75,58,0) 75%),
  radial-gradient(ellipse 90px 140px at 145px 230px,#9fb4c6,rgba(159,180,198,0) 75%),
  linear-gradient(180deg,#ffffff 0%,#e8f0f6 40%,#c4d4e1 75%,#9aaab8 100%)}
.svc-automotive{left:810px;top:210px}
.svc-automotive .photo{background:
  radial-gradient(ellipse 90px 70px at 120px 110px,#c99b7e,rgba(201,155,126,0) 75%),
  radial-gradient(ellipse 200px 150px at 200px 230px,#101010,rgba(16,16,16,0) 80%),
  linear-gradient(150deg,#f0f0f0 0%,#bdbdbd 35%,#5c5c5c 65%,#1a1a1a 100%)}

/* Testimonials */
.testimonials{top:2240px;height:580px;background:
  radial-gradient(circle at 180px 140px,rgba(255,255,255,.06) 0,rgba(255,255,255,.06) 180px,rgba(0,0,0,0) 182px),
  radial-gradient(ellipse at 50% 40%,#d3142f 0%,#a50d25 70%,#7e0a1b 100%)}
.testimonials .eyebrow{margin-top:42px}
.testimonials .section-title{margin-top:2px}
.avatar{position:absolute;border-radius:50%;border:3px solid var(--white)}
.av1{background:radial-gradient(circle at 50% 40%,#d9a98a 0 30%,#4d6b52 32%,#2e4433 100%)}
.av2{background:radial-gradient(circle at 50% 40%,#c78f6b 0 30%,#d8d2c6 32%,#a79e90 100%)}
.av3{background:radial-gradient(circle at 50% 40%,#e0b193 0 30%,#b94a3c 32%,#7a2b22 100%)}
.av4{background:radial-gradient(circle at 50% 40%,#a9745a 0 30%,#8899a8 32%,#56636f 100%)}
.av5{background:radial-gradient(circle at 50% 38%,#d8a283 0 28%,#6a4a3a 30%,#2f3a44 70%,#1e252c 100%)}
.av6{background:radial-gradient(circle at 50% 40%,#e5bc9e 0 30%,#c9b9a3 32%,#8f7e69 100%)}
.av7{background:radial-gradient(circle at 50% 40%,#c48a68 0 30%,#3c3c3c 32%,#1d1d1d 100%)}
.av8{background:radial-gradient(circle at 50% 40%,#e8c0a3 0 30%,#dcdcdc 32%,#a3a3a3 100%)}
.av9{background:radial-gradient(circle at 50% 40%,#b98066 0 30%,#b7653f 32%,#6e3a23 100%)}
.review{position:absolute;left:0;top:310px;width:1200px;text-align:center}
.review h4{font-family:"Poppins",sans-serif;font-weight:700;font-size:20px;text-transform:uppercase}
.stars{display:flex;justify-content:center;gap:4px;margin:8px 0 16px}
.review p{width:880px;margin:0 auto;font-size:14px;line-height:1.65;color:#f3dede}
.review-dots{position:absolute;left:560px;top:500px;display:flex;gap:10px}
.review-dots i{width:10px;height:10px;border-radius:50%;background:rgba(255,255,255,.45);display:block}
.review-dots i.on{background:var(--white)}

/* Contact */
.contact{top:2820px;height:520px;background:var(--black)}
.contact .eyebrow,.contact .section-title{text-align:left;position:absolute;left:110px;margin:0}
.contact .eyebrow{top:60px}
.contact .section-title{top:84px;font-size:34px}
.contact-form{position:absolute;left:110px;top:160px;width:560px;display:grid;grid-template-columns:1fr 1fr;gap:26px 40px}
.field{border-bottom:1px solid #555;padding-bottom:14px;font-size:13px}
.field.wide{grid-column:1/3;padding-bottom:34px}
.contact-form .btn{width:150px;text-align:center;padding:14px 0}
.contact-card{position:absolute;left:725px;top:55px;width:360px;height:330px;background:var(--red);padding:38px 32px}
.contact-card h3{font-family:"Poppins",sans-serif;font-weight:700;font-size:26px;line-height:1.3}
.contact-card p{font-size:14px;line-height:1.6;margin-top:24px;font-weight:700}
.dot-grid{position:absolute;left:1030px;top:365px}

/* Footer */
.footer{top:3340px;height:596px;background:var(--black)}
.footer-chevron{position:absolute;left:0;top:0}
.footer-brand{position:absolute;left:495px;top:70px;width:210px;height:100px;background:var(--red);border:3px solid var(--white);border-radius:12px;display:flex;align-items:center;justify-content:center}
.footer-brand .brand-name{font-size:20px;line-height:1.1;text-align:center}
.footer-cols{position:absolute;left:110px;top:230px;width:980px;display:flex}
.footer-col h5{font-family:"Poppins",sans-serif;font-weight:700;font-size:18px;text-transform:uppercase;margin-bottom:22px}
.footer-col ul{list-style:none;font-size:14px}
.footer-col li{margin-bottom:12px;display:flex;align-items:center;gap:10px}
.footer-col li::before{content:"";width:7px;height:7px;background:var(--white);transform:rotate(45deg)}
.footer-col.info li::before{display:none}
.footer-col .ic{width:26px;height:26px;flex:none;border-radius:50%;background:var(--white);display:flex;align-items:center;justify-content:center}
.col-quick{width:210px}.col-help{width:210px}.col-contact{width:270px}.col-about{width:290px}
.col-about p{font-size:13px;line-height:1.6;color:#ddd}
.col-about .social-row{display:flex;gap:12px;margin-top:18px}
.col-about .social-row i{width:34px;height:34px;border-radius:50%;background:var(--white);display:block}
.copyright{position:absolute;left:0;top:540px;width:1200px;text-align:center;font-size:13px;color:#ddd}
</style>
</head>
<body>

<header class="hero">
  <div class="hero-photo" role="img" aria-label="Hands applying window tint film to a glass pane"></div>
  <div class="hero-shade"></div>
  <div class="topbar"></div>
  <div class="social"><i></i><i></i><i></i><i></i></div>
  <div class="contact-mini">
    <span><svg width="14" height="14" viewBox="0 0 24 24"><path fill="#fff" d="M6.6 10.8a15 15 0 0 0 6.6 6.6l2.2-2.2a1 1 0 0 1 1-.25 11.4 11.4 0 0 0 3.6.57 1 1 0 0 1 1 1V20a1 1 0 0 1-1 1A17 17 0 0 1 3 4a1 1 0 0 1 1-1h3.5a1 1 0 0 1 1 1c0 1.25.2 2.45.57 3.57a1 1 0 0 1-.25 1z"/></svg>+1 000 000 0000</span>
    <span><svg width="15" height="12" viewBox="0 0 24 18"><rect x="1" y="1" width="22" height="16" rx="2" fill="none" stroke="#fff" stroke-width="2"/><path d="M1 2l11 8 11-8" fill="none" stroke="#fff" stroke-width="2"/></svg>info@apexshade.com</span>
  </div>
  <nav class="nav nav-left"><span class="active">Home</span><span>About</span><span>Services</span></nav>
  <div class="nav-brand"><div class="brand-name">Apex Shade<br>Tinting</div></div>
  <nav class="nav nav-right"><span>Testimonials</span><span class="btn btn-red">Contact Us</span></nav>

  <div class="hero-copy">
    <div class="kicker">WELCOME TO WINDOW TINTING</div>
    <h1>Your Window Film &amp; Paint Protection Specialists</h1>
    <p>Itaque earum rerum hic tenetur a sapiente delectus, ut aut reiciendis voluptatibus maiores repellat.</p>
    <span class="btn btn-white">Get Started</span>
  </div>
  <svg class="hero-chevron" width="1200" height="160" viewBox="0 0 1200 160">
    <polygon points="0,30 600,110 1200,30 1200,160 0,160" fill="#fff"/>
    <polyline points="0,18 600,98 1200,18" fill="none" stroke="#c8102e" stroke-width="18"/>
  </svg>
  <div class="slider-dots"><i class="on"></i><i></i></div>
</header>

<section class="about">
  <div class="eyebrow">Who We Are</div>
  <h2 class="section-title">About <span>Window</span> Tinting</h2>
  <div class="about-brand"><div class="brand-name"><i></i>Apex Shade</div></div>
  <div class="about-text">
    <p>Temporibus autem quibusdam et aut officiis debitis aut rerum necessitatibus saepe eveniet ut et voluptates repudiandae sint et molestiae non recusandae.</p>
    <p>Itaque earum rerum hic tenetur a sapiente delectus, ut aut reiciendis voluptatibus maiores alias consequatur aut perferendis doloribus asperiores repellat.</p>
    <span class="btn">Read More</span>
  </div>
  <div class="stats">
    <div class="stat"><strong>15k+</strong><span>More Than<br>Windows Tinted</span></div>
    <div class="stat"><strong>98%</strong><span>Hundreds of Happy Patients<br>with 98% Success Rate</span></div>
    <div class="stat"><strong>15 yr</strong><span>Built on 15 Years of<br>Experience</span></div>
    <div class="stat"><strong>10+</strong><span>Certified in Apex Shade<br>tinted</span></div>
  </div>
</section>

<section class="services">
  <div class="eyebrow">What We Offer</div>
  <h2 class="section-title">Our <span>Services</span></h2>
  <div class="service svc-commercial">
    <div class="photo" role="img" aria-label="Installer tinting a commercial office window"></div>
    <h3>Commercial Tinting</h3>
    <p>Temporibus autem quibusdam et aut officiis eveniet ut et voluptates repudiandae sint et molestiae non recusandae.</p>
  </div>
  <div class="service svc-residential">
    <div class="photo" role="img" aria-label="Installer applying film to a residential window"></div>
    <h3>Residential Tinting</h3>
    <p>Itaque earum rerum hic tenetur a sapiente delectus, ut aut reiciendis voluptatibus maiores alias consequatur.</p>
  </div>
  <div class="service svc-automotive">
    <div class="photo" role="img" aria-label="Technician tinting a car side window"></div>
    <h3>Automotive Tinting</h3>
    <p>Nam libero tempore, cum soluta nobis est eligendi optio cumque nihil impedit minus id quod maxime.</p>
  </div>
</section>

<section class="testimonials">
  <div class="eyebrow">Testimonials</div>
  <h2 class="section-title">What Customer Says</h2>
  <div class="avatar av1" role="img" aria-label="Customer portrait" style="left:110px;top:160px;width:64px;height:64px"></div>
  <div class="avatar av2" role="img" aria-label="Customer portrait" style="left:205px;top:220px;width:60px;height:60px"></div>
  <div class="avatar av3" role="img" aria-label="Customer portrait" style="left:320px;top:150px;width:64px;height:64px"></div>
  <div class="avatar av4" role="img" aria-label="Customer portrait" style="left:420px;top:225px;width:56px;height:56px"></div>
  <div class="avatar av5" role="img" aria-label="Customer portrait" style="left:545px;top:150px;width:110px;height:110px"></div>
  <div class="avatar av6" role="img" aria-label="Customer portrait" style="left:700px;top:220px;width:60px;height:60px"></div>
  <div class="avatar av7" role="img" aria-label="Customer portrait" style="left:810px;top:150px;width:64px;height:64px"></div>
  <div class="avatar av8" role="img" aria-label="Customer portrait" style="left:915px;top:220px;width:58px;height:58px"></div>
  <div class="avatar av9" role="img" aria-label="Customer portrait" style="left:1025px;top:160px;width:64px;height:64px"></div>
  <div class="review">
    <h4>Robert</h4>
    <div class="stars">
      <svg width="90" height="16" viewBox="0 0 90 16"><g fill="#fff"><path id="s" d="M8 0l2.4 5 5.6.8-4 3.9 1 5.5L8 12.6 3 15.2l1-5.5-4-3.9 5.6-.8z"/><use href="#s" x="18"/><use href="#s" x="36"/><use href="#s" x="54"/><use href="#s" x="72"/></g></svg>
    </div>
    <p>"Neque porro quisquam est, qui dolorem ipsum quia dolor sit amet, consectetur, adipisci velit, sed quia non numquam eius modi tempora incidunt ut labore et dolore magnam aliquam quaerat voluptatem. Ut enim ad minima veniam, quis nostrum exercitationem ullam corporis suscipit laboriosam nisi ut aliquid ex ea commodi consequatur."</p>
  </div>
  <div class="review-dots"><i></i><i></i><i class="on"></i><i></i><i></i></div>
</section>

<section class="contact">
  <div class="eyebrow">Contact Us</div>
  <h2 class="section-title">Get In Touch <span>With Us</span></h2>
  <form class="contact-form">
    <div class="field">Name</div>
    <div class="field">Email</div>
    <div class="field">Email</div>
    <div class="field">Address</div>
    <div class="field wide">Message</div>
    <span class="btn btn-red">Submit</span>
  </form>
  <div class="contact-card">
    <h3>Get In Touch With Us Itaque earum rerum hic tenetur a sapiente</h3>
    <p>Itaque earum rerum hic tenetur a sapiente delectus, ut aut reiciendis voluptatibus maiores doloribus asperiores repellat.</p>
  </div>
  <svg class="dot-grid" width="90" height="90" viewBox="0 0 90 90"><g fill="#c8102e">
    <circle cx="5" cy="5" r="3"/><circle cx="25" cy="5" r="3"/><circle cx="45" cy="5" r="3"/><circle cx="65" cy="5" r="3"/><circle cx="85" cy="5" r="3"/>
    <circle cx="5" cy="25" r="3"/><circle cx="25" cy="25" r="3"/><circle cx="45" cy="25" r="3"/><circle cx="65" cy="25" r="3"/><circle cx="85" cy="25" r="3"/>
    <circle cx="5" cy="45" r="3"/><circle cx="25" cy="45" r="3"/><circle cx="45" cy="45" r="3"/><circle cx="65" cy="45" r="3"/><circle cx="85" cy="45" r="3"/>
    <circle cx="5" cy="65" r="3"/><circle cx="25" cy="65" r="3"/><circle cx="45" cy="65" r="3"/><circle cx="65" cy="65" r="3"/><circle cx="85" cy="65" r="3"/>
    <circle cx="5" cy="85" r="3"/><circle cx="25" cy="85" r="3"/><circle cx="45" cy="85" r="3"/><circle cx="65" cy="85" r="3"/><circle cx="85" cy="85" r="3"/>
  </g></svg>
</section>

<footer class="footer">
  <svg class="footer-chevron" width="1200" height="200" viewBox="0 0 1200 200">
    <polyline points="0,130 600,20 1200,130" fill="none" stroke="#c8102e" stroke-width="16"/>
    <polyline points="0,190 600,80 1200,190" fill="none" stroke="#c8102e" stroke-width="4"/>
  </svg>
  <div class="footer-brand"><div class="brand-name">Apex Shade<br>Tinting</div></div>
  <div class="footer-cols">
    <div class="footer-col col-quick"><h5>Quick Links</h5>
      <ul><li>Home</li><li>About</li><li>Services</li><li>Testimonials</li><li>Contact Us</li></ul></div>
    <div class="footer-col col-help"><h5>Help Links</h5>
      <ul><li>FAQ</li><li>Terms of use</li><li>Privacy Policy</li><li>Support Links</li><li>Conditions</li></ul></div>
    <div class="footer-col col-contact info"><h5>Contact Us</h5>
      <ul>
        <li><span class="ic"><svg width="12" height="14" viewBox="0 0 24 30"><path fill="#0b0b0b" d="M12 0a11 11 0 0 0-11 11c0 8 11 19 11 19s11-11 11-19A11 11 0 0 0 12 0zm0 15a4 4 0 1 1 0-8 4 4 0 0 1 0 8z"/></svg></span>Window Tinting<br>United States</li>
        <li><span class="ic"><svg width="12" height="12" viewBox="0 0 24 24"><path fill="#0b0b0b" d="M6.6 10.8a15 15 0 0 0 6.6 6.6l2.2-2.2a1 1 0 0 1 1-.25 11.4 11.4 0 0 0 3.6.57 1 1 0 0 1 1 1V20a1 1 0 0 1-1 1A17 17 0 0 1 3 4a1 1 0 0 1 1-1h3.5a1 1 0 0 1 1 1c0 1.25.2 2.45.57 3.57a1 1 0 0 1-.25 1z"/></svg></span>+1 000 000 0000</li>
        <li><span class="ic"><svg width="13" height="10" viewBox="0 0 24 18"><rect x="1" y="1" width="22" height="16" rx="2" fill="none" stroke="#0b0b0b" stroke-width="2.5"/><path d="M1 2l11 8 11-8" fill="none" stroke="#0b0b0b" stroke-width="2.5"/></svg></span>info@apexshade.com</li>
      </ul></div>
    <div class="footer-col col-about"><h5>About Window Tinting</h5>
      <p>Itaque earum rerum hic tenetur a sapiente delectus, ut aut reiciendis voluptatibus maiores alias consequatur aut perferendis doloribus asperiores repellat.</p>
      <div class="social-row"><i></i><i></i><i></i><i></i></div>
    </div>
  </div>
  <div class="copyright">Copyright@2023Window Tinting. All Rights Reserved</div>
</footer>

</body>
</html>
```